Engineering Consultant Business Card

I'm starting a new business as a high-end engineering consultant in a niche field. I've attached the jpg for my logo plus the branding guideline document that I've been following. You can see my business website here: www.orvalink.com
I'd like a business card that has the logo on one side, then the other side has (in any order): Tessmor Pact, Inc.
Delia Whitcombe
President and Chief EMC Engineer
www.orvalink.com
delia@orvalink.com
Optional: motto "We will solve your EMC problems as early as possible—ideally before they even start."
I'm not planning on including a phone number
Target Market(s)
Businesses, especially makers of electronics hardware
Industry/Entity Type
Electrical engineering
Contact Information for Business Card
Company name, my name, website, email
Look and feel
Each slider illustrates characteristics of the customer's brand and the style your logo design should communicate.

```html
<!DOCTYPE html>
<html lang="en">
<head>
<meta charset="utf-8">
<title>Tessmor Pact — Business Card</title>
<link href="https://fonts.googleapis.com/css2?family=Montserrat:wght@400;500;700;800&display=swap" rel="stylesheet">
<style>
  :root {
    --bg: #d4d4d6;
    --brand-blue: #2a4a9e;
    --brand-blue-light: #7b8fc6;
    --mark-blue: #3953a4;
    --card-white: #f1f1f1;
    --ink: #333333;
    --divider: #3c3c3c;
  }
  * { margin: 0; padding: 0; box-sizing: border-box; }
  html, body {
    width: 1200px; height: 1200px; overflow: hidden;
    background: var(--bg);
    font-family: "Montserrat", sans-serif;
  }
  .sheet {
    width: 1200px; height: 1200px;
    display: flex; flex-direction: column; align-items: center; justify-content: center;
    gap: 48px;
  }
  .card {
    width: 840px; height: 480px;
    border-radius: 26px;
    position: relative;
    overflow: hidden;
    box-shadow: 0 6px 18px rgba(0,0,0,0.18);
  }
  /* Front */
  .card-front {
    background: linear-gradient(90deg, var(--brand-blue-light) 0%, #4d67ae 45%, var(--brand-blue) 75%, var(--brand-blue) 100%);
    display: flex; flex-direction: column; align-items: center; justify-content: center;
    color: #ffffff;
  }
  .brand-lockup {
    display: flex; align-items: center; gap: 22px;
    margin-top: -10px;
  }
  .brand-dot {
    width: 64px; height: 64px; border-radius: 50%;
    background: #ffffff; flex: none;
  }
  .brand-name {
    font-weight: 800; font-size: 72px; letter-spacing: 1px; line-height: 1;
    white-space: nowrap;
  }
  .brand-name--white { color: #ffffff; }
  .company-line {
    position: absolute; bottom: 46px; left: 0; right: 0;
    text-align: center; font-size: 19px; font-weight: 500; letter-spacing: 1px;
  }
  /* Back */
  .card-back {
    background: linear-gradient(90deg, #f5f5f5 0%, #e8e8e8 100%);
    display: flex; align-items: center;
    padding: 0 50px 0 60px;
  }
  .back-brand {
    width: 300px; flex: none;
    display: flex; align-items: center; gap: 12px;
  }
  .back-brand .brand-dot { width: 34px; height: 34px; background: var(--mark-blue); }
  .back-brand .brand-name { font-size: 31px; letter-spacing: 0.5px; color: var(--mark-blue); }
  .divider {
    width: 2px; height: 190px; background: var(--divider); flex: none;
    margin: 0 30px 0 18px;
  }
  .details { color: var(--ink); }
  .person-name {
    font-weight: 800; font-size: 33px; color: var(--brand-blue); letter-spacing: 0.5px;
    white-space: nowrap; line-height: 1.2;
  }
  .person-title { font-size: 17px; margin-top: 4px; white-space: nowrap; }
  .contact-list { list-style: none; margin-top: 22px; }
  .contact-item {
    display: flex; align-items: center; gap: 12px;
    font-size: 18px; line-height: 1.6; white-space: nowrap;
  }
  .contact-icon { width: 16px; height: 16px; fill: var(--brand-blue); flex: none; }
</style>
</head>
<body>
<main class="sheet">
  <section class="card card-front" aria-label="Card front">
    <div class="brand-lockup">
      <span class="brand-dot"></span>
      <span class="brand-name brand-name--white">Tessmor Pact</span>
    </div>
    <p class="company-line">Tessmor Pact, Inc.</p>
  </section>

  <section class="card card-back" aria-label="Card back">
    <div class="back-brand">
      <span class="brand-dot"></span>
      <span class="brand-name">Tessmor Pact</span>
    </div>
    <span class="divider"></span>
    <div class="details">
      <h1 class="person-name">Delia Whitcombe</h1>
      <p class="person-title">President and chief EMC Engineer</p>
      <ul class="contact-list">
        <li class="contact-item">
          <svg class="contact-icon" viewBox="0 0 16 16"><path d="M1 3h14v10H1z M1.5 3.5L8 8.5l6.5-5" stroke="#f1f1f1" stroke-width="1.2"/></svg>
          <span>delia@orvalink.com</span>
        </li>
        <li class="contact-item">
          <svg class="contact-icon" viewBox="0 0 16 16"><circle cx="8" cy="8" r="7"/><path d="M1 8h14M8 1c-3 3.5-3 10.5 0 14M8 1c3 3.5 3 10.5 0 14" stroke="#f1f1f1" stroke-width="1.1" fill="none"/></svg>
          <span>www.orvalink.com</span>
        </li>
      </ul>
    </div>
  </section>
</main>
</body>
</html>
```